Sole practitioner CPA needs stationery design work

I need design art work for stationery which I can take to my printer. I require letterhead, business card, with comp's slip ,envelope. I would also like a word template in the letterhead format, as well as an email signature.
There are some professional requirements regarding the Tallywise Institute motif, and the words "Liability limited by a scheme approved under Professional Standards legislation". I have attached a mock up letterhead which shows these items

Target Market(s)

Small business owners who will expect to see a professional image

Industry/Entity Type

Business

Requirements
Must have
• Must have TWI logo and the words "Liability limited by a scheme approved under Professional Standards Legislation".
Nice to have
• I have attached a 'sample" that has the logo and the words. But the sample scheme is not important.

```html
<!DOCTYPE html>
<html lang="en">
<head>
<meta charset="utf-8">
<title>Harlow Accounting Letterhead</title>
<link rel="stylesheet" href="https://fonts.googleapis.com/css2?family=Arimo:ital,wght@0,400;0,700;1,400&display=swap">
<style>
  :root {
    --brand-gold: #e8a93a;
    --brand-orange: #e07048;
    --rule-red: #d9684a;
    --ink: #111111;
    --muted-ink: #444444;
    --paper: #ffffff;
  }
  html, body {
    margin: 0;
    padding: 0;
    overflow: hidden;
    background: var(--paper);
  }
  .letterhead {
    position: relative;
    width: 927px;
    height: 1200px;
    background: var(--paper);
    overflow: hidden;
    font-family: "Arimo", Arial, sans-serif;
  }
  .brand-mark {
    position: absolute;
    left: 55px;
    top: 30px;
    width: 136px;
    height: 140px;
  }
  .brand-name {
    position: absolute;
    left: 222px;
    top: 22px;
    margin: 0;
    font-weight: 700;
    font-size: 74px;
    line-height: 1;
    letter-spacing: -2px;
    color: var(--brand-gold);
    white-space: nowrap;
  }
  .header-rule {
    position: absolute;
    left: 205px;
    top: 114px;
    width: 668px;
    height: 7px;
    background: var(--rule-red);
  }
  .contact-block {
    position: absolute;
    left: 193px;
    top: 125px;
    width: 684px;
    margin: 0;
    font-style: italic;
    font-size: 20.5px;
    line-height: 25px;
    letter-spacing: 0.2px;
    color: var(--ink);
    text-align: center;
    white-space: nowrap;
  }
  .contact-block p {
    margin: 0;
  }
  .footer {
    position: absolute;
    left: 55px;
    right: 55px;
    bottom: 40px;
    display: flex;
    align-items: center;
    justify-content: space-between;
    padding-top: 12px;
    border-top: 2px solid var(--rule-red);
  }
  .institute {
    display: flex;
    align-items: center;
    gap: 10px;
    font-size: 16px;
    font-weight: 700;
    color: var(--ink);
  }
  .institute-square {
    width: 20px;
    height: 20px;
    background: var(--brand-orange);
  }
  .liability-note {
    margin: 0;
    font-size: 13px;
    color: var(--muted-ink);
  }
</style>
</head>
<body>
  <div class="letterhead">
    <svg class="brand-mark" viewBox="0 0 136 140" aria-hidden="true">
      <circle cx="68" cy="70" r="66" fill="var(--brand-orange)"/>
    </svg>
    <h1 class="brand-name">Harlow Accounting</h1>
    <div class="header-rule"></div>
    <address class="contact-block">
      <p>14 Marlin Street, Larkfield, WA, 6999 PO Box 418, Larkfield, WA, 6999</p>
      <p>Phone: +61-8-55501234 Fax:&nbsp; +61-8-55501235</p>
      <p>Email Add. info@harlowaccounting.com.au</p>
    </address>
    <footer class="footer">
      <div class="institute">
        <span class="institute-square"></span>
        <span>Tallywise Institute</span>
      </div>
      <p class="liability-note">Liability limited by a scheme approved under Professional Standards Legislation</p>
    </footer>
  </div>
</body>
</html>
```